LoftVane Enterprises Corp., Contractor Tandem Dump Truck, Skidrow Services and 24/7 QuickRun Services

I need to ensure my LoftVane Enterprises Logo is eye catching on the front side. I would like to emphasize the services we supply on the front with eye catching Contractor Tandem Dump Trucks, Skidrows and also offer 24/7 QuickRun Services
Name: Glen Abernathy (owner /Manager), Address: Box 4 Site 7 RR5 Cochrane Alberta Canada T6K-3B8 - Office: 403-555-0172 Cell: 403-555-0248
email: loftvaneenterprisescochrane@mailbox-example.net, Website: www.loftvaneenterprises-example.com
Would like a nice Matt finish card, now you know why I needed 2 sided cards

```html
<!DOCTYPE html>
<html lang="en">
<head>
<meta charset="utf-8">
<title>LoftVane Enterprises Corp. – Business Card</title>
<link href="https://fonts.googleapis.com/css2?family=Arimo:wght@400;700&display=swap" rel="stylesheet">
<style>
  :root {
    --brand-orange: #cc7f30;
    --paper-white: #ffffff;
    --ink: #1c1c1c;
    --backdrop: #1e1e1e;
  }
  * { box-sizing: border-box; margin: 0; padding: 0; }
  html, body {
    width: 1189px; height: 1200px; overflow: hidden;
    background: var(--backdrop);
    font-family: "Arimo", Arial, sans-serif;
  }
  .card {
    position: absolute; left: 124px;
    width: 940px; height: 537px;
  }
  .card-front { top: 38px; background: var(--brand-orange); color: var(--paper-white); text-align: center; }
  .card-back { top: 625px; background: var(--paper-white); color: var(--ink); }

  .front-brand {
    position: absolute; top: 170px; left: 0; width: 100%;
    font-size: 44px; font-weight: 400; letter-spacing: 1px;
  }
  .front-services {
    position: absolute; top: 345px; left: 0; width: 100%;
    font-size: 23px; line-height: 29px;
  }

  .back-brand {
    position: absolute; top: 175px; right: 50px;
    font-size: 30px; font-weight: 400; color: var(--brand-orange);
    text-align: right;
  }
  .holder { position: absolute; left: 42px; top: 308px; }
  .holder-name { font-size: 29px; font-weight: 700; color: var(--brand-orange); text-transform: uppercase; line-height: 34px; }
  .holder-title { font-size: 22px; line-height: 26px; }
  .divider { position: absolute; left: 43px; right: 50px; top: 382px; height: 2px; background: var(--brand-orange); }
  .contact { position: absolute; left: 44px; top: 408px; font-size: 22px; line-height: 29px; }
  .label, .accent { color: var(--brand-orange); font-weight: 700; }
  .address { position: absolute; right: 50px; top: 413px; font-size: 22px; line-height: 29px; text-align: right; font-style: normal; }
</style>
</head>
<body>
  <section class="card card-front">
    <div class="front-brand">LoftVane Enterprises Corp.</div>
    <p class="front-services">Tandem Dump Truck Skidrow Services &amp; Contracting<br>24/7 QuickRun Services</p>
  </section>

  <section class="card card-back">
    <div class="back-brand">LoftVane Enterprises Corp.</div>
    <div class="holder">
      <div class="holder-name">Glen Abernathy</div>
      <div class="holder-title">Manager</div>
    </div>
    <div class="divider"></div>
    <div class="contact">
      <div><span class="label">Office:</span> 403-555-0172 | <span class="label">Cell:</span> 403-555-0248</div>
      <div><span class="label">Email:</span> loftvaneenterprisescochrane@mailbox-example.net</div>
      <div>www.<span class="accent">loftvaneenterprises-example</span>.com</div>
    </div>
    <address class="address">Box 4 Site 7 RR5<br>Cochrane Alberta<br>Canada T6K-3B8</address>
  </section>
</body>
</html>
```